SEAFOOD PACKAGING (Products for consumer)

We are looking to create packaging for various seafood products such as octopus and squid. We plan to sell our products in upscale supermarkets.

We are specializing in cut octopus this time.

Please include our company logo. Also, please leave a transparent area so that customers can see the product inside.
Updates

We want to show what is inside, so a picture of the octopus is not required. We need something simple and sophisticated.

Target Market(s)

upscale store in US and ASIA

Industry/Entity Type

Fisheries dealer

Requirements
Must have
• Please include the attached logo,Blue one is preferred.Please leave a transparent part so that the contents of the product can be seen by the consumer.1. product name on packaging →CUT OCTOPUS,TAKO SASHIMI,Highest quality,Top quality etc... 3. What text information should be on the packaging →(It may be edited, but this is the image) The raw materials are caught in a very clean environment and processed in a modern factory with ZEK certification. We are committed to additive-free products. 4. Packing size(cm/inch)→it will be about 19cm*22cm. 5. what kind of packaging do you use →PP or PA 6. dll →ai,jag
Nice to have
• https://quillmora.example/shots/4829174-Velka-Reef We need something simple and sophisticated like this one.
Should not have
• We want to show what is inside, so a picture of the octopus is not required. We need something simple and sophisticated.

```html
<!DOCTYPE html>
<html lang="en">
<head>
<meta charset="utf-8">
<title>Cut Octopus Pack</title>
<link rel="stylesheet" href="https://fonts.googleapis.com/css2?family=Oswald:wght@600;700&family=Open+Sans:wght@600;700&display=swap">
<style>
  :root {
    --bg: #f1f1f1;
    --pack-white: #ffffff;
    --sky-blue: #1c88d0;
    --navy: #213a8f;
    --brand-blue: #0e5ba8;
    --gold: #b88a2a;
    --octopus-deep: #5a1f3a;
    --octopus-red: #a8324e;
    --octopus-pale: #d9a3ad;
  }
  html, body { margin: 0; padding: 0; overflow: hidden; }
  body {
    width: 1200px; height: 1096px;
    background: var(--bg);
    position: relative;
    font-family: "Open Sans", sans-serif;
  }
  .pack {
    position: absolute; left: 300px; top: 170px;
    width: 600px; height: 730px;
    background: var(--pack-white);
    overflow: hidden;
  }
  .pack-art { position: absolute; inset: 0; }
  .frozen-tag {
    position: absolute; right: 30px; top: 46px;
    display: flex; align-items: center; gap: 10px;
    color: var(--pack-white); font-weight: 600; font-size: 18px; letter-spacing: 0.5px;
  }
  .premium {
    position: absolute; left: 38px; top: 98px;
    font-weight: 700; font-size: 38px; color: var(--gold); letter-spacing: 1px;
  }
  .product-name {
    position: absolute; left: 36px; top: 130px;
    font-family: "Oswald", sans-serif; font-weight: 700;
    font-size: 84px; line-height: 1; color: var(--sky-blue);
  }
  .product-sub {
    position: absolute; left: 180px; top: 228px;
    font-family: "Oswald", sans-serif; font-weight: 700;
    font-size: 38px; color: var(--brand-blue);
  }
  .brand {
    position: absolute; left: 96px; top: 300px;
    display: flex; align-items: center; gap: 26px;
  }
  .brand-dot { width: 74px; height: 74px; border-radius: 50%; background: var(--navy); }
  .brand-name {
    font-family: "Oswald", sans-serif; font-weight: 700;
    font-size: 96px; letter-spacing: 12px; color: var(--brand-blue); line-height: 1;
  }
  .serving {
    position: absolute; left: 30px; top: 618px;
    color: var(--pack-white); font-weight: 600; font-size: 20px;
  }
  .badges { position: absolute; left: 30px; top: 648px; display: flex; gap: 4px; }
  .badge {
    width: 42px; height: 46px; border-radius: 12px;
    background: var(--navy); border: 2px solid var(--pack-white);
    color: var(--pack-white); text-align: center;
    display: flex; flex-direction: column; justify-content: center;
  }
  .badge.wide { width: 50px; }
  .badge-value { font-family: "Oswald", sans-serif; font-weight: 700; font-size: 20px; line-height: 1; }
  .badge-label { font-size: 6px; font-weight: 600; margin-top: 3px; }
  .net-weight {
    position: absolute; right: 40px; top: 650px;
    font-family: "Oswald", sans-serif; font-weight: 700; font-size: 30px;
    color: var(--pack-white);
  }
</style>
</head>
<body>
  <div class="pack">
    <svg class="pack-art" viewBox="0 0 600 730" width="600" height="730">
      <defs>
        <linearGradient id="contents" x1="0" y1="0" x2="1" y2="1">
          <stop offset="0" stop-color="var(--octopus-red)"/>
          <stop offset="0.5" stop-color="var(--octopus-deep)"/>
          <stop offset="0.8" stop-color="var(--octopus-pale)"/>
          <stop offset="1" stop-color="var(--octopus-red)"/>
        </linearGradient>
      </defs>
      <path class="top-band" d="M160,0 L600,0 L600,95 C500,90 430,100 350,96 C260,92 210,50 160,0Z" fill="var(--sky-blue)"/>
      <path class="top-stripe" d="M175,0 C230,55 290,78 360,80 C440,82 520,76 600,76 L600,95 C500,90 430,100 350,96 C260,92 210,50 160,0Z" fill="var(--navy)"/>
      <path class="window" role="img" aria-label="Clear window showing frozen cut octopus pieces"
            d="M0,250 C40,380 120,470 230,470 C360,470 450,425 600,432 L600,730 L0,730Z" fill="url(#contents)"/>
      <path class="window-edge" d="M60,380 C110,440 160,470 230,470 C360,470 450,425 600,432 L600,418 C450,410 360,452 230,455 C150,456 100,425 60,380Z" fill="var(--navy)"/>
    </svg>

    <div class="frozen-tag">
      <svg width="30" height="30" viewBox="0 0 30 30" stroke="#fff" stroke-width="3" stroke-linecap="round">
        <line x1="15" y1="2" x2="15" y2="28"/><line x1="4" y1="8" x2="26" y2="22"/><line x1="4" y1="22" x2="26" y2="8"/>
      </svg>
      FROZEN PRODUCT
    </div>
    <div class="premium">PREMIUM</div>
    <div class="product-name">Cut Octopus</div>
    <div class="product-sub">TAKO SASHIMI</div>
    <div class="brand">
      <span class="brand-dot"></span>
      <span class="brand-name">MARIVO</span>
    </div>
    <div class="serving">PER SERVING</div>
    <div class="badges">
      <div class="badge"><span class="badge-value">76</span><span class="badge-label">CALORIES</span></div>
      <div class="badge"><span class="badge-value">0g</span><span class="badge-label">SAT FAT</span></div>
      <div class="badge wide"><span class="badge-value">220</span><span class="badge-label">SODIUM mg</span></div>
      <div class="badge"><span class="badge-value">0g</span><span class="badge-label">SUGAR</span></div>
    </div>
    <div class="net-weight">500G</div>
  </div>
</body>
</html>
```